Business Card and Letterhead for Nurlo - modern real estate business

I need a double sided business card design for Nurlo. Please see business card brief here https://papers.trelvimo.net/sheet/q/7XrTbaLeZpMmQ2uWvd9HkCj4yNoEfsGi3lRtAz_pk/view?mode=shared

Please feel free to design the business cards however you feel best. I am happy to give some creative freedoms and then provide feedback from there.

Please then also create a letterhead to match the business card design

Colors

Designer to choose colors to be used in the design.

Requirements
Must have
• Must be a modern, elegant business card which looks very professional

```html
<!DOCTYPE html>
<html lang="en">
<head>
<meta charset="utf-8">
<title>Nurlo — Business Card and Letterhead</title>
<link href="https://fonts.googleapis.com/css2?family=Lato:wght@400;700&display=swap" rel="stylesheet">
<style>
  :root {
    --brand-red: #e31d2b;
    --ink-black: #161616;
    --paper-white: #ffffff;
    --body-text: #1c1c1c;
    --card-text: #f2f2f2;
    --backdrop: #e8e5e0;
    --photo-tone-a: #9aa58a;
    --photo-tone-b: #3d4436;
  }
  * { box-sizing: border-box; margin: 0; padding: 0; }
  html, body { width: 1200px; height: 900px; overflow: hidden; }
  body {
    background: var(--backdrop);
    font-family: "Lato", Arial, sans-serif;
    position: relative;
  }

  /* Letterhead */
  .letterhead {
    position: absolute; left: 132px; top: 112px;
    width: 493px; height: 698px;
    background: var(--paper-white);
    box-shadow: 0 4px 12px rgba(0,0,0,.25);
    overflow: hidden;
  }
  .letterhead__header { position: absolute; left: 0; top: 0; width: 493px; height: 80px; }
  .letterhead__header svg { display: block; width: 100%; height: 100%; }
  .letterhead__brand {
    position: absolute; left: 16px; top: 42px;
    font-size: 40px; font-weight: 700; letter-spacing: 1px;
    color: var(--brand-red); line-height: 1;
  }
  .letter {
    position: absolute; left: 47px; top: 177px; width: 401px;
    font-size: 9.6px; line-height: 12px; color: var(--body-text);
  }
  .letter__greeting { margin-bottom: 17px; }
  .letter__para { text-align: justify; margin-bottom: 24px; }
  .letter__signoff { line-height: 13.2px; margin-top: 0; }
  .letterhead__footer {
    position: absolute; left: 0; bottom: 0; width: 100%; height: 27px;
    background: var(--ink-black); color: var(--card-text);
    font-size: 9.6px; display: flex; align-items: center; justify-content: center;
    gap: 6px; padding-left: 16px;
  }

  /* Business cards */
  .card {
    position: absolute; width: 409px;
    background: var(--ink-black);
    box-shadow: 0 4px 10px rgba(0,0,0,.3);
  }
  .card--front { left: 713px; top: 169px; height: 245px; }
  .card--back { left: 712px; top: 461px; height: 248px; display: flex; align-items: center; justify-content: center; }

  .card__photo {
    position: absolute; left: 35px; top: 51px; width: 144px; height: 144px;
    border-radius: 50%; border: 2px solid var(--brand-red);
    background: radial-gradient(circle at 50% 40%, var(--photo-tone-a), var(--photo-tone-b));
  }
  .card__divider {
    position: absolute; left: 205px; top: 53px; width: 1.5px; height: 139px;
    background: var(--brand-red);
  }
  .card__details { position: absolute; left: 227px; top: 56px; color: var(--card-text); }
  .card__name { font-size: 19px; font-weight: 700; color: var(--brand-red); line-height: 22px; }
  .card__role { font-size: 11.5px; line-height: 16px; margin-top: 1px; }
  .card__address { font-size: 11.5px; line-height: 13.5px; margin-top: 10px; }
  .card__contacts { list-style: none; margin-top: 9px; font-size: 11.5px; }
  .card__contacts li { display: flex; align-items: center; gap: 9px; height: 15.6px; }
  .card__contacts svg { width: 11px; height: 11px; flex: none; }

  .card__brand {
    font-size: 80px; font-weight: 700; letter-spacing: 3px;
    color: var(--brand-red); line-height: 1;
  }
</style>
</head>
<body>

<section class="letterhead">
  <div class="letterhead__header">
    <svg viewBox="0 0 822 134" preserveAspectRatio="none" aria-hidden="true">
      <rect width="822" height="134" fill="#161616"/>
      <path d="M0,56 C260,44 600,58 822,128 L822,134 L0,134 Z" fill="#ffffff"/>
      <path d="M0,36 C300,26 620,46 790,116 C610,62 270,46 0,58 Z" fill="#e31d2b"/>
    </svg>
  </div>
  <div class="letterhead__brand">NURLO</div>

  <div class="letter">
    <p class="letter__greeting">Dear Sir/Mam,</p>
    <p class="letter__para">Contrary to popular belief, Lorem Ipsum is not simply random text. It has roots in a piece of classical Latin literature from 45 BC, making it over 2000 years old. Rowan Mercer, a Latin professor at Harlow-Ridge College in Virginia, looked up one of the more obscure Latin words, consectetur, from a Lorem Ipsum passage, and going through the cites of the word in classical literature, discovered the undoubtable source.</p>
    <p class="letter__para">Lorem Ipsum comes from sections 1.10.32 and 1.10.33 of "de Finibus Bonorum et Malorum" (The Extremes of Good and Evil) by Corvinus, written in 45 BC. This book is a treatise on the theory of ethics, very popular during the Renaissance. The first line of Lorem Ipsum, "Lorem ipsum dolor sit amet..", comes from a line in section 1.10.32.</p>
    <p class="letter__para">The standard chunk of Lorem Ipsum used since the 1500s is reproduced below for those interested. Sections 1.10.32 and 1.10.33 from "de Finibus Bonorum et Malorum" by Corvinus are also reproduced in their exact original form, accompanied by English versions from the 1914 translation by H. Ransford.</p>
    <p class="letter__para">The standard chunk of Lorem Ipsum used since the 1500s is reproduced below for those interested.</p>
    <p class="letter__signoff">Best Regards<br>Liam Carver<br>Licenced Real Estate Agent</p>
  </div>

  <footer class="letterhead__footer">
    <span>0491 570 318</span><span>|</span><span>liam@nurlo.com</span><span>&nbsp;|</span><span>www.nurlo.com</span><span>&nbsp;|</span><span>PO Box 3917. Glenmoor NSW 2790</span>
  </footer>
</section>

<section class="card card--front">
  <div class="card__photo" role="img" aria-label="Portrait photo of the agent, outdoors with a green valley behind"></div>
  <div class="card__divider"></div>
  <div class="card__details">
    <h1 class="card__name">Liam Carver</h1>
    <p class="card__role">Licenced Real Estate Agent</p>
    <p class="card__address">PO Box 3917<br>Glenmoor NSW 2790</p>
    <ul class="card__contacts">
      <li>
        <svg viewBox="0 0 24 24" aria-hidden="true"><path fill="#e31d2b" d="M6.6 10.8a15.1 15.1 0 0 0 6.6 6.6l2.2-2.2c.3-.3.7-.4 1-.2 1.1.4 2.3.6 3.6.6.6 0 1 .4 1 1V20c0 .6-.4 1-1 1A17 17 0 0 1 3 4c0-.6.4-1 1-1h3.5c.6 0 1 .4 1 1 0 1.2.2 2.4.6 3.6.1.3 0 .7-.2 1z"/></svg>
        <span>0491 570 318</span>
      </li>
      <li>
        <svg viewBox="0 0 24 24" aria-hidden="true"><rect x="2" y="5" width="20" height="14" fill="#e31d2b"/><path d="M2 5l10 8 10-8" fill="none" stroke="#161616" stroke-width="2"/></svg>
        <span>liam@nurlo.com</span>
      </li>
      <li>
        <svg viewBox="0 0 24 24" aria-hidden="true"><g fill="none" stroke="#e31d2b" stroke-width="2"><circle cx="12" cy="12" r="9"/><path d="M3 12h18M12 3c3 3 3 15 0 18M12 3c-3 3-3 15 0 18"/></g></svg>
        <span>www.nurlo.com</span>
      </li>
    </ul>
  </div>
</section>

<section class="card card--back">
  <div class="card__brand">NURLO</div>
</section>

</body>
</html>
```